Velvet Harbour Sessions

Need to improve polish and professionalism of PPT presentation. Get consistent look and feel through whole slides, improved look and feel while maintaining the corporate standards/colour scheme, from the Brimwells corporate presentation. Need everything in Arial font with colours consistent with the PPT template

```html
<!DOCTYPE html>
<html lang="en">
<head>
<meta charset="utf-8">
<title>Velvet Harbour Sessions – KPIs &amp; Production Fundamentals</title>
<link href="https://fonts.googleapis.com/css2?family=Arimo:wght@400;700&display=swap" rel="stylesheet">
<style>
:root{
  --ink:#0f2229;
  --red:#d3282f;
  --grey:#9aa4ac;
  --green:#3e8b2c;
  --yellow:#fff200;
  --purple:#7b2b6c;
  --paper:#ffffff;
  --text:#1b1b1b;
  --muted:#a9b2b6;
}
*{box-sizing:border-box;margin:0;padding:0}
html,body{width:720px;height:1200px;overflow:hidden;background:var(--paper)}
body{font-family:Arimo,Arial,sans-serif;color:var(--text)}
.deck{position:absolute;left:0;top:0;width:1484px;height:2480px;transform:scale(0.4839);transform-origin:0 0}
.slide{position:absolute;width:679px;height:382px;background:var(--paper);overflow:hidden}
.col-a{left:61px}.col-b{left:754px}
.r0{top:65px}.r1{top:461px}.r2{top:857px}.r3{top:1253px}.r4{top:1649px}.r5{top:2045px}

/* cover */
.cover{background:var(--ink)}
.cover .brand{position:absolute;left:62px;top:48px;font-size:44px;font-weight:700;color:#fff;letter-spacing:1px}
.cover .deck-title{position:absolute;left:59px;top:152px;font-size:27px;color:#fff;letter-spacing:.5px}
.cover .deck-sub{position:absolute;left:59px;top:188px;font-size:21px;font-weight:700;color:var(--red)}
.cover .legal{position:absolute;right:24px;top:358px;font-size:7px;color:var(--muted)}

/* heading */
.mark{position:absolute;left:0;top:35px;width:21px;height:19px;background:var(--ink)}
.heading{position:absolute;left:50px;top:31px;font-size:22px;font-weight:700;color:var(--red)}
.intro{position:absolute;left:50px;font-size:12.5px}

/* footer */
.footer{position:absolute;left:0;bottom:0;width:679px;height:28px;background:var(--ink)}
.footer .brand{position:absolute;left:31px;top:7px;font-size:12px;font-weight:700;color:#fff;letter-spacing:.5px}
.footer .legal{position:absolute;left:246px;top:10px;font-size:6.5px;color:var(--muted)}
.page-no{position:absolute;left:630px;top:346px;width:25px;height:36px;background:var(--red);color:#fff;font-size:6px;text-align:center;padding-top:20px}

/* bullets */
.points{position:absolute;left:50px;width:590px;list-style:none;font-size:8.3px;line-height:1.6}
.points li{position:relative;padding-left:16px}
.points li::before{content:"✦";position:absolute;left:0;top:-1px;color:var(--red);font-size:10px}
.points li.sub{padding-left:39px;font-size:5.4px;line-height:1.9}
.points li.sub::before{left:16px;font-size:7px;top:0}
.points li.plain::before{content:none}
.points li.gap{margin-top:10px}
.points b{font-weight:700}

/* time usage model */
.tum{position:absolute;left:50px;width:578px;height:125px;background:var(--grey)}
.cell{position:absolute;display:flex;align-items:center;justify-content:center;font-size:7.5px;color:#fff;background:var(--ink);border:1px solid #fff;text-align:center}
.cell.down{background:var(--red);font-size:6.5px}
.cell.stop{background:var(--red)}
.cell.delay{background:var(--green)}
.cell.standby{background:var(--yellow);color:var(--ink);font-weight:700}
.cell.idle{background:var(--purple)}
.calendar{left:20px;top:20px;width:538px;height:22px}
.available{left:20px;top:41px;width:360px;height:22px}
.down{left:380px;top:41px;width:178px;height:10px}
.unsched{left:380px;top:50px;width:89px;height:56px}
.sched{left:469px;top:50px;width:89px;height:56px}
.operating{left:20px;top:62px;width:180px;height:22px}
.delay{left:200px;top:62px;width:90px;height:44px}
.standby{left:290px;top:62px;width:90px;height:44px}
.effective{left:20px;top:84px;width:90px;height:22px}
.non-effective{left:110px;top:84px;width:90px;height:22px}
.pointer{position:absolute;left:0;top:0}

/* tree */
.tree{position:absolute;left:50px;width:341px;height:103px}
.node{position:absolute;height:35px;width:131px;border-radius:9px;background:var(--ink);color:#fff;font-weight:700;font-size:13px;display:flex;align-items:center;justify-content:center;text-align:center;line-height:1.15}
.node.focus{background:var(--red)}
.node.root{left:80px;top:0}
.node.left{left:0;top:68px}
.node.right{left:160px;top:68px}
.tree svg{position:absolute;left:0;top:0}
</style>
</head>
<body>
<div class="deck">

  <!-- 1 cover -->
  <section class="slide cover col-a r0">
    <div class="brand">BRIMWELLS</div>
    <div class="deck-title">VELVET HARBOUR SESSIONS</div>
    <div class="deck-sub">KPIs &amp; Production Fundamentals</div>
    <div class="legal">© 2024 Brimwells Mining Solutions Inc. &nbsp;&nbsp;&nbsp; Strictly Confidential</div>
  </section>

  <!-- 2 -->
  <section class="slide col-a r1">
    <div class="mark"></div><h2 class="heading">KPIs &amp; Production Fundamentals</h2>
    <p class="intro" style="top:78px">At the end of this module, you will understand</p>
    <ul class="points" style="top:104px">
      <li>Understand the key concepts of mine production KPIs</li>
      <li>Time Usage Model</li>
      <li class="sub">Availability, Utilization and Productivity</li>
      <li class="sub">Elements of the haul cycle</li>
      <li class="sub">Elements of the loading cycle</li>
      <li class="sub">How changes in each of these elements impact mine production</li>
      <li>The goal will be to create a baseline of understanding and a common language across the entire mine-ops team</li>
      <li>You may already understand these concepts</li>
      <li>This is the time to ask questions and get clarification!</li>
    </ul>
    <footer class="footer"><span class="brand">BRIMWELLS</span><span class="legal">© 2024 Brimwells Mining Solutions Inc. &nbsp;&nbsp;&nbsp; Strictly Confidential</span></footer>
    <div class="page-no">2</div>
  </section>

  <!-- 3 -->
  <section class="slide col-a r2">
    <div class="mark"></div><h2 class="heading">What Makes up Production</h2>
    <p class="intro" style="top:77px">In its simplest terms, we calculate production like this:</p>
    <div class="tree" style="top:116px">
      <svg width="341" height="70"><path d="M145 35V58M65 68V58H225V68" stroke="#0f2229" stroke-width="1.3" fill="none"/></svg>
      <div class="node root">PRODUCTION</div>
      <div class="node left">Equipment<br>Productivity</div>
      <div class="node right">Operating<br>Time</div>
    </div>
    <ul class="points" style="top:242px">
      <li>This is true for any process</li>
      <li class="sub">Mowing the lawn</li>
      <li class="sub">Driving</li>
      <li class="sub">Mine Production</li>
      <li>Production goes up or down because of a change in <b>Equipment Productivity</b> or <b>Operating Time</b></li>
    </ul>
    <footer class="footer"><span class="brand">BRIMWELLS</span><span class="legal">© 2024 Brimwells Mining Solutions Inc. &nbsp;&nbsp;&nbsp; Strictly Confidential</span></footer>
    <div class="page-no">3</div>
  </section>

  <!-- 4 -->
  <section class="slide col-a r3">
    <div class="mark"></div><h2 class="heading">What Makes up Production</h2>
    <p class="intro" style="top:77px">At its simplest terms, we calculate production like this:</p>
    <div class="tree" style="top:110px">
      <svg width="341" height="70"><path d="M145 35V58M65 68V58H225V68" stroke="#0f2229" stroke-width="1.3" fill="none"/></svg>
      <div class="node root">PRODUCTION</div>
      <div class="node left">Equipment<br>Productivity</div>
      <div class="node right focus">Operating<br>Time</div>
    </div>
    <ul class="points" style="top:240px">
      <li>Operating time is the time when a piece of equipment is performing it's <b>primary function</b></li>
      <li>To better understand, communicate and discuss the different categories of how we calculate operating time, we use something called a <b>Time Usage Model</b></li>
      <li>Each industry has its own time usage model, and they can vary slightly from industry to industry</li>
      <li>Even within an industry, (e.g. Mining) a Time Usage Model can vary from operation to operation</li>
    </ul>
    <footer class="footer"><span class="brand">BRIMWELLS</span><span class="legal">© 2024 Brimwells Mining Solutions Inc. &nbsp;&nbsp;&nbsp; Strictly Confidential</span></footer>
    <div class="page-no">4</div>
  </section>

  <!-- 5 -->
  <section class="slide col-a r4">
    <div class="mark"></div><h2 class="heading">Generic Time Usage Model</h2>
    <div class="tum" style="top:78px">
      <div class="cell calendar">Calendar Time</div>
      <div class="cell available">Available Time</div>
      <div class="cell down">Down</div>
      <div class="cell stop unsched">Unscheduled</div>
      <div class="cell stop sched">Scheduled</div>
      <div class="cell operating">Operating Time</div>
      <div class="cell delay">Operating Delay</div>
      <div class="cell standby">Standby Time</div>
      <div class="cell effective">Effective Time</div>
      <div class="cell idle non-effective">Non-Effective Time</div>
    </div>
    <ul class="points" style="top:241px">
      <li>This is a generic Mining time usage model</li>
      <li>There may be variations from mine-to-mine (ie Utilized time vs Operating Time) but this model describes everything mine operations needs to know about the time usage of a piece of equipment</li>
    </ul>
    <footer class="footer"><span class="brand">BRIMWELLS</span><span class="legal">© 2024 Brimwells Mining Solutions Inc. &nbsp;&nbsp;&nbsp; Strictly Confidential</span></footer>
    <div class="page-no">5</div>
  </section>

  <!-- 6 -->
  <section class="slide col-a r5">
    <div class="mark"></div><h2 class="heading">TUM – Calendar Time</h2>
    <div class="tum" style="top:77px">
      <div class="cell calendar">Calendar Time</div>
      <svg class="pointer" width="578" height="125"><path d="M289 46L335 125H243Z" fill="#fff"/></svg>
    </div>
    <ul class="points" style="top:251px">
      <li>Calendar time means all the time in a period</li>
      <li class="sub">Calendar time for 1 Year = 365 Days</li>
      <li class="sub">Calendar time for October = 31 days</li>
      <li class="sub">Calendar time for 1 shift = 12 hours</li>
    </ul>
    <footer class="footer"><span class="brand">BRIMWELLS</span><span class="legal">© 2024 Brimwells Mining Solutions Inc. &nbsp;&nbsp;&nbsp; Strictly Confidential</span></footer>
    <div class="page-no">6</div>
  </section>

  <!-- 7 -->
  <section class="slide col-b r0">
    <div class="mark"></div><h2 class="heading">TUM – Available Time</h2>
    <div class="tum" style="top:75px">
      <div class="cell calendar">Calendar Time</div>
      <div class="cell available">Available Time</div>
      <div class="cell down">Down</div>
      <div class="cell stop unsched">Unscheduled</div>
      <div class="cell stop sched">Scheduled</div>
      <svg class="pointer" width="578" height="125"><path d="M289 67L323 125H255Z" fill="#fff"/></svg>
    </div>
    <ul class="points" style="top:222px">
      <li>Available Time is the time a piece of equipment (or fleet) is mechanically available to operate</li>
      <li>Available Time = Calendar Time – Down Time</li>
      <li>Downtime can be</li>
      <li class="sub">Planned (PMs, Rebuilds)</li>
      <li class="sub">Unplanned (Breakdown, Accident Damage)</li>
      <li>Availability % = Available Time / Calendar Time</li>
    </ul>
    <footer class="footer"><span class="brand">BRIMWELLS</span><span class="legal">© 2024 Brimwells Mining Solutions Inc. &nbsp;&nbsp;&nbsp; Strictly Confidential</span></footer>
    <div class="page-no">7</div>
  </section>

  <!-- 8 -->
  <section class="slide col-b r1">
    <div class="mark"></div><h2 class="heading">TUM – Operating Time</h2>
    <div class="tum" style="top:78px">
      <div class="cell calendar">Calendar Time</div>
      <div class="cell available">Available Time</div>
      <div class="cell down">Down</div>
      <div class="cell stop unsched">Unscheduled</div>
      <div class="cell stop sched">Scheduled</div>
      <div class="cell operating">Operating Time</div>
      <div class="cell delay">Operating Delay</div>
      <div class="cell standby">Standby Time</div>
      <svg class="pointer" width="578" height="125"><path d="M290 106L300 125H280Z" fill="#fff"/></svg>
    </div>
    <ul class="points" style="top:221px">
      <li><b>Operating Time is the time where the equipment (or fleet) is working as planned</b></li>
      <li>It excludes periods of standby and operating delays</li>
      <li>Standby time is typically time where the piece of equipment isn't required to operate</li>
      <li class="sub">This could be because there isn't work to do (No Shovel, No Muck)</li>
      <li class="sub">It could also be because there is nobody to operate the machine (No Operator)</li>
      <li class="plain">Operating Delay occurs when the equipment is required to operate but can't perform it's primary work function</li>
      <li class="sub">Fueling, Tramming, Moving</li>
      <li class="sub">As a rule of thumb, if there is a 'butt in the seat,' it is considered an operating delay, not a standby</li>
      <li>Utilization % = Operating Time / Available Time</li>
      <li>Some sites refer to this as Use of Availability % or UofA %</li>
    </ul>
    <footer class="footer"><span class="brand">BRIMWELLS</span><span class="legal">© 2024 Brimwells Mining Solutions Inc. &nbsp;&nbsp;&nbsp; Strictly Confidential</span></footer>
    <div class="page-no">8</div>
  </section>

  <!-- 9 -->
  <section class="slide col-b r2">
    <div class="mark"></div><h2 class="heading">TUM – Effective Time</h2>
    <div class="tum" style="top:78px">
      <div class="cell calendar">Calendar Time</div>
      <div class="cell available">Available Time</div>
      <div class="cell down">Down</div>
      <div class="cell stop unsched">Unscheduled</div>
      <div class="cell stop sched">Scheduled</div>
      <div class="cell operating">Operating Time</div>
      <div class="cell delay">Operating Delay</div>
      <div class="cell standby">Standby Time</div>
      <div class="cell effective">Effective Time</div>
      <div class="cell idle non-effective">Non-Effective Time</div>
    </div>
    <ul class="points" style="top:221px">
      <li><b>Effective Time is the time when the equipment is doing its productive activities</b></li>
      <li>It excludes waiting/idle time that is included in operating time</li>
      <li>This waiting/idle, non-effective time is a part of the regular operation of the machine, but is not productive</li>
      <li class="sub">Shovel Hang</li>
      <li class="sub">Truck wait @ dump or wait @ shovel</li>
      <li>Effective Utilization % = Effective Time / Available Time</li>
      <li>OEE % = Effective Time / Calendar Time</li>
    </ul>
    <footer class="footer"><span class="brand">BRIMWELLS</span><span class="legal">© 2024 Brimwells Mining Solutions Inc. &nbsp;&nbsp;&nbsp; Strictly Confidential</span></footer>
    <div class="page-no">9</div>
  </section>

  <!-- 10 -->
  <section class="slide col-b r3">
    <div class="mark"></div><h2 class="heading">TUM - Summary</h2>
    <div class="tum" style="top:78px">
      <div class="cell calendar">Calendar Time</div>
      <div class="cell available">Available Time</div>
      <div class="cell down">Down</div>
      <div class="cell stop unsched">Unscheduled</div>
      <div class="cell stop sched">Scheduled</div>
      <div class="cell operating">Operating Time</div>
      <div class="cell delay">Operating Delay</div>
      <div class="cell standby">Standby Time</div>
      <div class="cell effective">Effective Time</div>
      <div class="cell idle non-effective">Non-Effective Time</div>
    </div>
    <ul class="points" style="top:221px">
      <li>The Time Usage Model is a way of describing how time for equipment is allocated over a period (shift/month/year)</li>
      <li class="gap">Availability % = What percentage of the shift/month/year is the equipment down?</li>
      <li>Availability % = Available Time / Calendar Time</li>
      <li class="gap">Utilization % = What percentage of the time the equipment is available is it Operating?</li>
      <li>Utilization % = Operating Time / Available Time</li>
    </ul>
    <footer class="footer"><span class="brand">BRIMWELLS</span><span class="legal">© 2024 Brimwells Mining Solutions Inc. &nbsp;&nbsp;&nbsp; Strictly Confidential</span></footer>
    <div class="page-no">10</div>
  </section>

  <!-- 11 -->
  <section class="slide col-b r4">
    <div class="mark"></div><h2 class="heading">What Makes up Production</h2>
    <p class="intro" style="top:78px">In its simplest terms, we calculate production like this:</p>
    <div class="tree" style="top:117px">
      <svg width="341" height="70"><path d="M145 35V58M65 68V58H225V68" stroke="#0f2229" stroke-width="1.3" fill="none"/></svg>
      <div class="node root">PRODUCTION</div>
      <div class="node left focus">Equipment<br>Productivity</div>
      <div class="node right">Operating<br>Time</div>
    </div>
    <ul class="points" style="top:260px">
      <li>The other side of production is Equipment Productivity</li>
      <li>This metric describes how PRODUCTIVE the equipment is during the operating time</li>
      <li>For this course, we will focus on productivity of <b>Trucks</b> and <b>Shovels</b></li>
    </ul>
    <footer class="footer"><span class="brand">BRIMWELLS</span><span class="legal">© 2024 Brimwells Mining Solutions Inc. &nbsp;&nbsp;&nbsp; Strictly Confidential</span></footer>
    <div class="page-no">11</div>
  </section>

  <!-- 12 -->
  <section class="slide col-b r5">
    <div class="mark"></div><h2 class="heading">Equipment Productivity – Haul Trucks</h2>
    <div class="tree" style="top:95px">
      <svg width="341" height="70"><path d="M146 35V58M65 68V58H225V68" stroke="#0f2229" stroke-width="1.3" fill="none"/></svg>
      <div class="node root" style="left:38px;width:216px">EQUIPMENT PRODUCTIVITY</div>
      <div class="node left">Cycle Time</div>
      <div class="node right focus">Tonnes per Cycle</div>
    </div>
    <ul class="points" style="top:249px">
      <li>For haul trucks, tonnes per cycle is simply Payload</li>
      <li>The higher the payload, the higher the equipment productivity</li>
      <li>What are the limitations of Payload?</li>
    </ul>
    <footer class="footer"><span class="brand">BRIMWELLS</span><span class="legal">© 2024 Brimwells Mining Solutions Inc. &nbsp;&nbsp;&nbsp; Strictly Confidential</span></footer>
    <div class="page-no">12</div>
  </section>

</div>
</body>
</html>
```